Gutschein-Design zur Pflegeberatung
Zielgruppe
Wir feiern mit unserem Pflegedienst das 10 Jährige Jubiläum. Da es wegen der Corona Pandemie keine Feierlichkeiten geben kann, würde ich wir einen Gutschein für eine kostenlose Pflegeberatung erstellen lassen. Auf die Vorderseite bitte den Gutschein mit dem Text:
Bilder bitte aus den öffentlichen Portalen verwenden.
Gutschein zur Pflegeberatung
Wir unterstützen bei der Beantragung eines Pflegegrades und helfen bei abgelehnten Anträgen.
Gerne informieren wir Sie über umfangreiche Möglichkeiten der ambulante Pflege und erstellen einen individuellen Versorgungsplan. Darüber hinaus erhalte Sie praktische Tipps zu Alltagshilfen und konkrete Hilfestellungen rund um die Pflege, damit Sie noch so lange wie möglich zu
Hause bleiben können.
Unten bitte einfügen: Gutschein gültig bis einschließlich Juli 2022
Auf die Rückseite bitte eine kurze Info zu unserem 10 Jährigen bestehen.
Vielleicht vielleicht wieder mit dem Slogan, Seit 10 Jahren rund um die Uhr für Sie im Einsatz.
Aufgabenstellung
Da wir zwei ambulante Filialen betreiben, muss das Logo auf die zweite Filiale angepasst werden.
Der Text und die Informationen bleiben jedoch gleich. Der Gutschein sollte sofort auffallen und animieren, im Pflegedienst anzurufen.

```html
<!DOCTYPE html>
<html lang="de">
<head>
<meta charset="utf-8">
<title>Gutschein zur Pflegeberatung – Pflegehaus Lindenhof</title>
<link rel="stylesheet" href="https://fonts.googleapis.com/css2?family=Lobster&family=Nunito:wght@400;700;800;900&display=swap">
<style>
  :root {
    --green: #3aa54a;
    --blue: #1f4f9c;
    --orange: #ea8a2b;
    --ink: #1d1d1d;
    --paper: #ffffff;
    --stage: #efefef;
    --photo-light: #e9eef5;
    --photo-mid: #b9cbe3;
    --photo-warm: #d9d2c8;
  }
  * { box-sizing: border-box; margin: 0; padding: 0; }
  html, body { width: 909px; height: 1200px; overflow: hidden; }
  body {
    background: var(--stage);
    font-family: "Nunito", Arial, sans-serif;
    color: var(--ink);
    position: relative;
  }
  .card {
    position: absolute;
    left: 34px;
    width: 840px;
    height: 370px;
    background: var(--paper);
    overflow: hidden;
    box-shadow: 0 6px 14px rgba(0,0,0,.18);
  }
  .card--front { top: 18px; }
  .card--back-single { top: 415px; }
  .card--back-duo { top: 812px; }

  .photo {
    position: absolute;
    top: 0;
    right: 0;
    height: 100%;
  }
  .photo--front {
    width: 520px;
    background: linear-gradient(90deg, var(--paper) 0%, var(--photo-light) 25%, var(--photo-mid) 65%, var(--photo-light) 100%);
  }
  .photo--back {
    width: 470px;
    background: linear-gradient(90deg, var(--paper) 0%, var(--photo-light) 30%, var(--photo-warm) 70%, var(--photo-light) 100%);
  }
  .photo-stack {
    position: absolute;
    top: 0;
    right: 0;
    width: 290px;
    height: 100%;
    display: grid;
    grid-template-rows: 1fr 1fr;
    gap: 6px;
    padding: 0 0 0 0;
  }
  .photo-stack .tile--a { background: linear-gradient(135deg, #e5e0d8, #c9d3df); }
  .photo-stack .tile--b { background: linear-gradient(135deg, #6fa6d6, #d8c8b0); }

  .headline {
    position: absolute;
    left: 34px;
    top: 30px;
    color: var(--green);
  }
  .headline__main {
    font-family: "Lobster", cursive;
    font-size: 72px;
    line-height: 1;
  }
  .headline__sub {
    font-weight: 800;
    font-size: 27px;
    margin: -6px 0 0 58px;
  }
  .body-copy {
    position: absolute;
    left: 34px;
    top: 150px;
    width: 380px;
    font-size: 13.2px;
    line-height: 1.42;
  }
  .valid-pill {
    position: absolute;
    left: 110px;
    bottom: 24px;
    background: var(--green);
    color: var(--paper);
    font-weight: 700;
    font-size: 15px;
    padding: 7px 22px;
    border-radius: 4px;
  }
  .band {
    position: absolute;
    left: 0;
    bottom: 0;
    width: 100%;
    height: 40px;
    background: var(--blue);
    color: var(--paper);
    display: flex;
    align-items: center;
  }
  .band__orange {
    position: absolute;
    right: 0;
    bottom: 0;
    height: 40px;
    background: var(--orange);
    color: var(--paper);
    display: flex;
    align-items: center;
    justify-content: center;
  }
  .card--front .band { width: 760px; justify-content: flex-end; padding-right: 24px; font-size: 13px; }
  .card--front .band__orange { width: 80px; height: 40px; }

  .brand-tile {
    position: absolute;
    right: 14px;
    bottom: 56px;
    width: 120px;
    height: 120px;
    background: var(--paper);
    border-radius: 16px;
    display: flex;
    flex-direction: column;
    align-items: center;
    justify-content: center;
    gap: 8px;
    text-align: center;
  }
  .brand-tile__dot {
    width: 34px; height: 34px; border-radius: 50%; background: var(--green);
  }
  .brand-tile__name {
    color: var(--green);
    font-weight: 800;
    font-size: 14px;
    line-height: 1.15;
  }

  .slogan {
    position: absolute;
    left: 34px;
    top: 26px;
    color: var(--green);
    font-weight: 800;
    font-size: 30px;
    line-height: 1.2;
  }
  .slogan strong { font-weight: 900; }
  .quote {
    position: absolute;
    left: 34px;
    top: 108px;
    width: 470px;
    font-size: 14px;
    line-height: 1.45;
  }
  .invite {
    position: absolute;
    left: 34px;
    top: 246px;
    width: 480px;
    font-size: 14.5px;
    line-height: 1.5;
  }
  .invite .phone { color: var(--green); font-weight: 800; font-size: 20px; }
  .card--back-single .band,
  .card--back-duo .band { width: 100%; padding-left: 24px; gap: 34px; font-size: 14px; font-weight: 700; }
  .card--back-single .band__orange,
  .card--back-duo .band__orange { width: 260px; font-weight: 700; font-size: 14px; }
</style>
</head>
<body>

<!-- Vorderseite -->
<section class="card card--front">
  <div class="photo photo--front" role="img" aria-label="Foto: Pflegekraft berät ein älteres Ehepaar am Tisch"></div>
  <div class="headline">
    <div class="headline__main">Gutschein</div>
    <div class="headline__sub">zur Pflegeberatung</div>
  </div>
  <p class="body-copy">Wir unterstützen bei der Beantragung eines Pflegegrades und helfen bei abgelehnten Anträgen. Gerne informieren wir Sie über umfangreiche Möglichkeiten der ambulante Pflege und erstellen einen individuellen Versorgungsplan. Darüber hinaus erhalte Sie praktische Tipps zu Alltagshilfen und konkrete Hilfestellungen rund um die Pflege, damit Sie noch so lange wie möglich zu. Hause bleiben können.</p>
  <div class="brand-tile">
    <span class="brand-tile__dot"></span>
    <span class="brand-tile__name">Pflegehaus<br>Lindenhof</span>
  </div>
  <div class="band">Weitere Informationen finden Sie auf der Rückseite</div>
  <div class="band__orange">
    <svg width="34" height="22" viewBox="0 0 34 22" aria-hidden="true">
      <path d="M3 19 C6 9 14 6 24 7" fill="none" stroke="#fff" stroke-width="3.5" stroke-linecap="round"/>
      <path d="M20 2 L29 7 L21 13" fill="none" stroke="#fff" stroke-width="3.5" stroke-linecap="round" stroke-linejoin="round"/>
    </svg>
  </div>
  <div class="valid-pill">gültig bis : &nbsp;einschließlich Juli 2022</div>
</section>

<!-- Rückseite, Variante mit einem Foto -->
<section class="card card--back-single">
  <div class="photo photo--back" role="img" aria-label="Foto: Pflegerin hilft einer lächelnden Seniorin beim Zuknöpfen der Bluse"></div>
  <h2 class="slogan">Seit <strong>10 Jahren</strong> rund um die<br>Uhr für Sie im Einsatz.</h2>
  <p class="quote">"Wir vom <strong>Pflegehaus Lindenhof</strong> sind ein Team dem die Individualität eines jeden Stärke verleiht und uns so das Selbstverständnis im Umgang mit der Einzigartigkeit jedes Patienten lehrt. Unser ambulanter Pflegedienst bietet Ihnen mit seinem Team erfahrener und motivierter Mitarbeiter ein Höchstmaß an Wohlbefinden und Eigenständigkeit sowie eine Entlastung Ihrer Angehörigen."</p>
  <p class="invite">Wir sind für Sie da und freuen uns auf ein persönliches Kennenlernen. Rufen Sie uns unter <span class="phone">0800 214 36 70</span> an.</p>
  <div class="band">
    <span>Lindenweg 7 18057 Hafenstadt</span>
    <span>info@pflegehaus-lindenhof.de</span>
  </div>
  <div class="band__orange">www.pflegehaus-lindenhof.de</div>
</section>

<!-- Rückseite, Variante mit zwei Fotos -->
<section class="card card--back-duo">
  <div class="photo-stack">
    <div class="tile--a" role="img" aria-label="Foto: Pflegerin hilft einer Seniorin beim Ankleiden"></div>
    <div class="tile--b" role="img" aria-label="Foto: Pflegerin in blauer Kleidung lacht mit einer Seniorin"></div>
  </div>
  <h2 class="slogan">Seit <strong>10 Jahren</strong> rund um die<br>Uhr für Sie im Einsatz.</h2>
  <p class="quote">"Wir vom <strong>Pflegehaus Lindenhof</strong> sind ein Team dem die Individualität eines jeden Stärke verleiht und uns so das Selbstverständnis im Umgang mit der Einzigartigkeit jedes Patienten lehrt. Unser ambulanter Pflegedienst bietet Ihnen mit seinem Team erfahrener und motivierter Mitarbeiter ein Höchstmaß an Wohlbefinden und Eigenständigkeit sowie eine Entlastung Ihrer Angehörigen."</p>
  <p class="invite">Wir sind für Sie da und freuen uns auf ein persönliches Kennenlernen. Rufen Sie uns unter <span class="phone">0800 214 36 70</span> an.</p>
  <div class="band">
    <span>Lindenweg 7 18057 Hafenstadt</span>
    <span>info@pflegehaus-lindenhof.de</span>
  </div>
  <div class="band__orange">www.pflegehaus-lindenhof.de</div>
</section>

</body>
</html>
```